SEO Company Needs a Professional, Bold Business Card Design

Vantor SEO
2847 N Larkfield Ave #415
Austin, TX 78712
512-384-2915
http://www.vantorseo.com
Vantor SEO is an internet marketing company specializing in SEO for higher-end businesses. We are looking for a professional and bold (edgy) design that communicates our forward thinking SEO strategies. Our typical client is a small to medium US business that has never had SEO work done on their website but does has active marketing. We want our business card design to instill confidence in our services through a professional and bold look. We we would also like the design elements to be in line with the services we offer - ranking client websites in the search engine results, namely Quarlo.
Design Specifics:
Card design should have square edges.
Design should be delivered in fully layered and editable PSD file. Designing in AI is fine but I need a PSD file in case we have any changes in contact information or need additional cards for employees.
The design should compliment the attached logo.
Company Name:
Vantor SEO
Address:
2847 N Larkfield Ave #415
Austin, TX 78712
Personal Info:
Gareth Doyle
Owner
thelead@vantorseo.com
Phone:
877-826-8677 (VANTORS)
Website:
http://www.vantorseo.com
Slogan:
Could Your Website Be Generating More Business?
Target Market(s)
High-end business owners - doctors, lawyers, specialists, business owners doing 250k in profit.
Industry/Entity Type
Internet
Contact Information for Business Card
Company Name:
Vantor SEO
Address:
456 Other Lane Ste 456
Austin, TX 78712
Personal Info:
Gareth Doyle
Owner
thelead@vantorseo.com
Phone:
877-826-8677 (VANTORS)
Website:
www.vantorseo.com
Slogan:
Requirements
Must have
- Card design should have square edges.
- Background should be WHITE only.
- Design should be delivered in fully layered and editable PSD file. Designing in AI is fine but I need a PSD file in case we have any changes in contact information or need additional cards for employees.

```html
<!DOCTYPE html>
<html lang="en">
<head>
<meta charset="utf-8">
<title>Vantor SEO Business Card</title>
<link href="https://fonts.googleapis.com/css2?family=Lato:wght@400;700;900&display=swap" rel="stylesheet">
<style>
  :root {
    --stage: #3b3b3b;
    --card-light: #ffffff;
    --card-shade: #e6e6e6;
    --accent-blue: #2a9fd6;
    --navy: #183f72;
    --cyan: #36bcd8;
    --cyan-deep: #1f8fc4;
    --text-dark: #3a3a3a;
    --web-red: #d8262b;
  }
  * { margin: 0; padding: 0; box-sizing: border-box; }
  html, body { width: 1200px; height: 750px; overflow: hidden; }
  body {
    background: var(--stage);
    font-family: "Lato", sans-serif;
    position: relative;
  }
  .card {
    position: absolute;
    top: 218px;
    width: 504px;
    height: 286px;
    background: radial-gradient(ellipse at 50% 40%, var(--card-light) 30%, var(--card-shade) 100%);
    overflow: hidden;
  }
  .card-front { left: 80px; }
  .card-back { left: 616px; }

  .person-name {
    position: absolute; left: 26px; top: 34px;
    font-size: 16.5px; font-weight: 700; color: var(--accent-blue);
  }
  .person-role {
    position: absolute; left: 26px; top: 54px;
    font-size: 12px; font-weight: 400; color: var(--text-dark);
  }
  .contact-list { position: absolute; left: 26px; top: 88px; list-style: none; }
  .contact-list li {
    display: flex; align-items: center; height: 14.5px;
    font-size: 12px; color: var(--text-dark);
  }
  .contact-list svg { width: 11px; height: 11px; margin-right: 8px; flex: none; }
  .web-name { color: var(--web-red); }
  .address {
    position: absolute; left: 26px; top: 152px;
    font-size: 12px; line-height: 14.5px; color: var(--text-dark);
  }
  .brand {
    position: absolute; display: flex; align-items: center;
    font-weight: 900; color: var(--navy); white-space: nowrap;
  }
  .brand-dot { border-radius: 50%; background: var(--navy); flex: none; }
  .brand-front { right: 20px; top: 62px; font-size: 30px; }
  .brand-front .brand-dot { width: 22px; height: 22px; margin-right: 8px; }
  .brand-back { left: 0; right: 0; justify-content: center; top: 100px; font-size: 44px; }
  .brand-back .brand-dot { width: 30px; height: 30px; margin-right: 12px; }
  .growth-band {
    position: absolute; left: 0; right: 0; bottom: 0; height: 96px;
    background: linear-gradient(90deg, var(--cyan-deep) 0%, var(--cyan) 45%, var(--navy) 100%);
  }
  .slogan {
    position: absolute; left: 0; right: 0; top: 187px; text-align: center;
    font-size: 12.5px; font-weight: 400; color: var(--navy);
  }
</style>
</head>
<body>
  <section class="card card-front">
    <h1 class="person-name">Gareth Doyle</h1>
    <p class="person-role">Owner</p>
    <ul class="contact-list">
      <li>
        <svg viewBox="0 0 12 12"><path d="M2.5 1 L4.5 1 L5 3.5 L3.8 4.5 Q5 7 7.5 8.2 L8.5 7 L11 7.5 L11 9.5 Q10 11 8 10.5 Q2 8.5 1 3 Q1 1.5 2.5 1Z" fill="var(--accent-blue)"/></svg>
        877-826-8677
      </li>
      <li>
        <svg viewBox="0 0 12 12"><rect x="0.5" y="2.5" width="11" height="7" fill="var(--accent-blue)"/><path d="M0.5 2.5 L6 6.5 L11.5 2.5" stroke="#fff" stroke-width="1" fill="none"/></svg>
        thelead@vantorseo.com
      </li>
      <li>
        <svg viewBox="0 0 12 12"><g fill="none" stroke="var(--accent-blue)" stroke-width="1"><circle cx="6" cy="6" r="5"/><ellipse cx="6" cy="6" rx="2.2" ry="5"/><path d="M1 6 H11 M2 3.5 H10 M2 8.5 H10"/></g></svg>
        <span>www.<span class="web-name">vantorseo</span>.com</span>
      </li>
    </ul>
    <p class="address">456 Other Lane Ste 456<br>Austin, TX 78712</p>
    <div class="brand brand-front"><span class="brand-dot"></span>Vantor SEO</div>
    <div class="growth-band" role="img" aria-label="Rising growth chart graphic in navy and cyan"></div>
  </section>

  <section class="card card-back">
    <div class="brand brand-back"><span class="brand-dot"></span>Vantor SEO</div>
    <p class="slogan">Could Your Website Be Generating More Business?</p>
  </section>
</body>
</html>
```